Web design for Digital Marketing Agency

Hello,
the name of our agency is "Bright Lantern" with the idea that we make Bright Lantern for our client count. You can find our logo attached. Use blue tone similar to it a modern sans serif form that fits the design.
We need a web design similar to this one:
https: // larkfield-studio. de /
What I like about this design:
- clear navigation with personalized Pic for phone number and clear call to action in nav bar (which is then repeated in hero image)
- the hero image having custom cartoon represtation giving a visual impression of what the company does (in our case paid adwords on different channels, like Wexly Ads, Tribbon etc; and analyzing data and optimizing the website based on that)
-a clear cut structure that goes on with similar cartoons when appropriate
- using bright background colors for sections
- lots of space so content can breath
The following sections are needed in this order:
-navbar
-hero image with text:
"Digital marketing for companies who know that Bright Lantern counts.
We always help you to achieve the best in every digital transaction. Because like in real life, you don't get a second channel for your first impression. "
Services Section:
1.) Paid advertising
2.) Analytics & Optimization
3.) Chatbots
4.) E-commerce shops
-Explaining the Service Secion (the section explaining the service that is chose by the user above 1/3 image / 2/3 text - image should also be a cartoon fitting in style to overall pic and representing the service that will be explained)
- Bright Lantern Concept
2 rings similar to above website
- the process section
- what customer are saying section
-contact form section
-footer
Target Market(s)
Companies seeking to increase sales online / generate new lead online. Main focus ecommerce but also traditional companies like real estate or lawyers
Number of Pages Required
1 page
Font styles to use
Look and feel
Each slider illustrates characteristics of the customer's brand and the style your logo design should communicate.

```html
<!DOCTYPE html>
<html lang="en">
<head>
<meta charset="utf-8">
<title>Bright Lantern – Digital Marketing</title>
<link rel="stylesheet" href="https://fonts.googleapis.com/css2?family=Baloo+2:wght@700;800&family=Poppins:wght@300;400;500;600&display=swap">
<style>
:root{
  --blue-deep:#1a56c9;
  --blue:#2b7fd4;
  --blue-sky:#35a3dc;
  --text-blue:#2f86d0;
  --card-text:#3d8fd6;
  --venn:#7cc6e6;
  --venn-core:#4fb0de;
  --pale:#e6f2fb;
  --line:#b9dcf2;
  --white:#ffffff;
  --grad:linear-gradient(135deg,var(--blue-sky) 0%,var(--blue) 45%,var(--blue-deep) 100%);
}
*{box-sizing:border-box;margin:0;padding:0}
html,body{width:1200px;height:4284px;overflow:hidden;background:var(--white)}
body{position:relative;font-family:"Poppins",sans-serif;color:var(--text-blue)}
.abs{position:absolute}
.display{font-family:"Baloo 2",sans-serif;font-weight:800;color:var(--blue)}

/* nav */
.nav-links{left:42px;top:45px;display:flex;gap:24px;font-size:13px}
.brand{display:flex;align-items:center;gap:10px;font-weight:600;color:var(--blue);letter-spacing:.5px}
.brand-dot{width:38px;height:38px;border-radius:50%;background:var(--blue)}
.nav-brand{left:478px;top:36px;font-size:18px}
.btn{display:flex;align-items:center;justify-content:center;border-radius:10px;font-size:15px;font-weight:500}
.btn-outline{left:844px;top:28px;width:150px;height:55px;border:2px solid var(--blue);color:var(--blue)}
.btn-fill{background:var(--grad);color:var(--white);box-shadow:0 6px 14px rgba(26,86,201,.25)}

/* hero */
.hero-phone{left:260px;top:166px;width:440px;height:350px;border-radius:40px;background:linear-gradient(160deg,#e9f4fc,#cfe6f7)}
.hero-scene{left:680px;top:183px;width:483px;height:450px;border-radius:60px;background:linear-gradient(160deg,#d6ebfa,#b7d6f3 60%,#e4f0fa)}
.hero-title{left:43px;top:296px;width:640px;font-size:28px;line-height:32px;font-weight:600;color:var(--blue-sky)}
.hero-copy{left:43px;top:372px;width:560px;font-size:18px;line-height:24px;color:var(--blue)}
.play{left:230px;top:476px;display:flex;align-items:center;gap:12px;font-size:16px;font-weight:500;color:var(--blue)}

/* services */
.section-title{font-size:38px;text-align:center;width:1200px;left:0}
.card{top:786px;width:259px;height:321px;border:2px solid var(--blue-sky);border-radius:16px;text-align:center;padding-top:44px}
.card svg{display:block;margin:0 auto}
.card h3{font-size:13px;font-weight:500;margin-top:24px;color:var(--card-text)}
.card p{font-size:10px;line-height:13px;width:216px;margin:6px auto 0;color:var(--card-text)}
.card.active{background:var(--grad);border-color:transparent}
.card.active h3,.card.active p{color:var(--white)}

/* concept */
.concept-title{left:620px;top:1250px;font-size:30px}
.concept-copy{left:620px;top:1304px;width:540px;font-size:14px;line-height:21.6px;font-weight:300;color:#6b8fb5}

/* process */
.process{left:0;top:1861px;width:1200px;height:544px;background:linear-gradient(110deg,var(--blue-sky) 0%,var(--blue) 50%,var(--blue-deep) 100%)}
.process .display{color:var(--white)}
.step-line{left:301px;top:2098px;width:600px;height:6px;background:rgba(255,255,255,.35)}
.step{width:110px;height:110px;border-radius:50%;background:var(--white);top:2046px}
.step-label{top:2178px;width:160px;text-align:center;color:var(--white);font-size:17px;font-weight:500}
.process-copy{left:250px;top:2258px;width:700px;text-align:center;color:var(--white);font-size:17px;line-height:20px}

/* testimonials */
.quote-art{left:17px;top:2626px;width:482px;height:424px;border-radius:120px 60px 140px 80px;background:linear-gradient(150deg,#e8f3fc,#d2e8f8)}
.quote-marks{left:770px;top:2880px;font-family:"Baloo 2",sans-serif;font-size:260px;line-height:1;color:#d9ecf8}
.quote-copy{left:610px;top:2772px;width:508px;text-align:center;font-size:17px;line-height:22px;color:#4a7fb8}
.quote-rule{left:620px;top:2945px;width:495px;height:1px;background:var(--line)}
.dot{top:3051px;width:12px;height:12px;border-radius:50%;background:var(--blue-sky)}

/* contact */
.field{border:2px solid var(--blue-sky);border-radius:6px;padding:16px 18px;font-size:16px;color:#8ba6c3}
.contact-art{left:790px;top:3324px;width:410px;height:241px;border-radius:40px;background:linear-gradient(180deg,#f4f8fc,#e4edf6)}

/* footer */
.footer{left:0;top:3768px;width:1200px;height:516px;background:linear-gradient(110deg,var(--blue-sky) 0%,var(--blue) 45%,var(--blue-deep) 100%)}
.footer-brand{left:410px;top:3820px;font-size:26px;color:var(--white)}
.footer-brand .brand-dot{background:var(--white);width:46px;height:46px}
.col{top:3908px;color:var(--white);font-size:22px;line-height:32.5px;font-weight:300}
.col h4{font-size:22px;font-weight:600}
.footer-art{left:798px;top:3906px;width:365px;height:265px;border-radius:30px;background:linear-gradient(160deg,rgba(255,255,255,.22),rgba(255,255,255,.08))}
.footer-rule{left:86px;top:4233px;width:1028px;height:1px;background:rgba(255,255,255,.5)}
.copyright{left:0;top:4244px;width:1200px;text-align:center;color:var(--white);font-size:14px}
</style>
</head>
<body>

<!-- navigation -->
<nav class="abs nav-links"><span>Our Team</span><span>Case Study</span><span>Contact Us</span><span>Careers</span></nav>
<div class="abs brand nav-brand"><span class="brand-dot"></span>BRIGHT LANTERN</div>
<div class="abs btn btn-outline">Call US</div>
<div class="abs btn btn-fill" style="left:1010px;top:30px;width:147px;height:52px">Get Started</div>

<!-- hero -->
<div class="abs hero-phone" role="img" aria-label="Illustration of a smartphone with a lightbulb, like and megaphone icons"></div>
<div class="abs hero-scene" role="img" aria-label="Illustration of two marketers at a desk analysing charts and dashboards"></div>
<h1 class="abs hero-title">Digital marketing for companies who know that Bright Lantern counts.</h1>
<p class="abs hero-copy">We always help you to achieve the best in every digital transaction. Because like in real life, you don't get a second channel for your first impression.</p>
<div class="abs btn btn-fill" style="left:43px;top:474px;width:145px;height:48px">Get Started</div>
<div class="abs play">
  <svg width="44" height="44" viewBox="0 0 44 44"><circle cx="22" cy="22" r="20" fill="none" stroke="#2b7fd4" stroke-width="2"/><path d="M17 13 L31 22 L17 31 Z" fill="none" stroke="#2b7fd4" stroke-width="2" stroke-linejoin="round"/></svg>
  PLAY VIDEO
</div>

<!-- services -->
<h2 class="abs section-title display" style="top:676px">Our Services</h2>

<div class="abs card" style="left:42px">
  <svg width="104" height="108" viewBox="0 0 104 108" fill="none" stroke="#2b7fd4" stroke-width="2.5"><rect x="2" y="2" width="100" height="64" rx="3"/><text x="52" y="46" text-anchor="middle" font-family="Poppins,sans-serif" font-size="26" fill="#2b7fd4" stroke="none">ADS</text><line x1="52" y1="66" x2="52" y2="106"/><path d="M10 76h84M16 66v14M88 66v14"/><line x1="36" y1="106" x2="68" y2="106"/></svg>
  <h3>Paid advertising</h3>
  <p>Campaigns on search and social channels built to reach buyers at the right moment, tuned every week for lower cost per lead and steady growth in sales.</p>
</div>
<div class="abs card" style="left:327px">
  <svg width="110" height="108" viewBox="0 0 110 108" fill="none" stroke="#2b7fd4" stroke-width="2.5"><rect x="2" y="2" width="106" height="76" rx="3"/><polyline points="16,58 36,38 54,52 74,28 92,40"/><line x1="55" y1="78" x2="55" y2="98"/><line x1="30" y1="100" x2="80" y2="100"/></svg>
  <h3>Analytics &amp; Optimization</h3>
  <p>We track every visit and click, read what the numbers say, and refine your pages so more visitors turn into customers who come back again and again.</p>
</div>
<div class="abs card active" style="left:615px">
  <svg width="60" height="108" viewBox="0 0 60 108" fill="none" stroke="#fff" stroke-width="2.5"><circle cx="30" cy="8" r="6"/><line x1="30" y1="14" x2="30" y2="24"/><rect x="12" y="24" width="36" height="26" rx="10"/><rect x="6" y="54" width="48" height="34" rx="8"/><rect x="14" y="88" width="32" height="16" rx="4"/></svg>
  <h3>Chatbots</h3>
  <p>Friendly chat assistants answer questions day and night, qualify new leads on the spot and hand warm contacts to your team without any delay or lost chances.</p>
</div>
<div class="abs card" style="left:899px">
  <svg width="106" height="108" viewBox="0 0 106 108" fill="none" stroke="#2b7fd4" stroke-width="2.5"><rect x="6" y="40" width="94" height="56" rx="3"/><line x1="2" y1="102" x2="104" y2="102"/><rect x="28" y="22" width="50" height="54"/><path d="M42 22v-8a11 11 0 0 1 22 0v8"/><path d="M50 46l12 8-6 2 4 8-3 1-4-8-4 4z"/></svg>
  <h3>E-commerce shops</h3>
  <p>Online shops that load fast, look great on any screen and make checkout simple, so browsing shoppers become loyal buyers who order from you again.</p>
</div>

<!-- concept -->
<svg class="abs" style="left:170px;top:1258px" width="270" height="390" viewBox="0 0 270 390">
  <circle cx="134" cy="130" r="129" fill="#7cc6e6"/>
  <circle cx="131" cy="259" r="129" fill="#7cc6e6" opacity=".9"/>
  <path d="M43 221 A129 129 0 0 1 220 222 A129 129 0 0 1 43 221 Z" fill="#4fb0de"/>
  <text x="134" y="88" text-anchor="middle" font-family="Poppins,sans-serif" font-size="15" fill="#fff">Conversion</text>
  <text x="132" y="200" text-anchor="middle" font-family="Poppins,sans-serif" font-size="14" font-weight="600" fill="#fff">Successful Business</text>
  <text x="131" y="308" text-anchor="middle" font-family="Poppins,sans-serif" font-size="15" font-weight="500" fill="#fff">Efficiency</text>
</svg>
<h2 class="abs concept-title display">Bright Lantern Concept</h2>
<p class="abs concept-copy">Lorem ipsum dolor sit amet, consectetur adipisicing elit, sed do eiusmod tempor incididunt ut labore et dolore magna aliqua. Ut enim ad minim veniam, quis nostrud exercitation ullamco laboris nisi ut aliquip ex ea commodo consequat. Duis aute irure dolor in reprehenderit in voluptate velit esse cillum dolore eu fugiat nulla pariatur. Excepteur sint occaecat cupidatat non proident, sunt in culpa qui officia deserunt mollit anim id est laborum. Sed ut perspiciatis unde omnis iste natus error sit voluptatem accusantium doloremque laudantium, totam rem aperiam, eaque ipsa quae ab illo inventore veritatis et quasi architecto beatae vitae dicta sunt explicabo. Nemo enim ipsam voluptatem quia voluptas sit aspernatur aut odit aut fugit, sed quia consequuntur magni dolores eos qui ratione voluptatem sequi nesciunt. Neque porro quisquam est,</p>
<div class="abs btn btn-fill" style="left:618px;top:1594px;width:147px;height:50px">Get Started</div>

<!-- process -->
<section class="abs process"></section>
<h2 class="abs section-title display" style="top:1930px;color:#fff;font-size:32px">Our Working Process</h2>
<div class="abs step-line"></div>
<div class="abs step" style="left:246px"></div>
<div class="abs step" style="left:445px"></div>
<div class="abs step" style="left:645px"></div>
<div class="abs step" style="left:846px"></div>
<div class="abs step-label" style="left:221px">Lorem Ipsum</div>
<div class="abs step-label" style="left:420px">Lorem Ipsum</div>
<div class="abs step-label" style="left:620px">Lorem Ipsum</div>
<div class="abs step-label" style="left:821px">Lorem Ipsum</div>
<p class="abs process-copy">Lorem ipsum dolor sit amet, consectetur adipisicing elit, sed do eiusmod tempor incididunt ut labore et dolore magna aliqua. Ut enim ad minim veniam, quis nostrud exercitation ullamco laboris nisi ut aliquip ex ea</p>

<!-- testimonials -->
<div class="abs quote-art" role="img" aria-label="Illustration of a customer sitting inside a large smartphone surrounded by leaves"></div>
<h2 class="abs display" style="left:620px;top:2652px;width:488px;text-align:center;font-size:40px;color:var(--blue-sky)">They Said</h2>
<div class="abs quote-marks">”</div>
<p class="abs quote-copy">Lorem ipsum dolor sit amet, consectetur adipisicing elit, sed do eiusmod tempor incididunt ut labore et dolore magna aliqua. Ut enim ad minim veniam, quis nostrud exercitation ullamco laboris nisi ut aliquip ex ea commodo consequat. Duis aute irure dolor in reprehenderit in voluptate velit esse cillum dolore eu fugiat nulla pariatur. Excepteur sint occaecat cupidatat non proident, sunt in culpa qui officia</p>
<div class="abs quote-rule"></div>
<div class="abs" style="left:620px;top:2983px;font-size:17px;font-weight:500;color:var(--blue)">Jonas Falk, Owner</div>
<div class="abs dot" style="left:835px"></div>
<div class="abs dot" style="left:857px;width:15px;height:15px;top:3049px;background:#23408e"></div>
<div class="abs dot" style="left:880px"></div>

<!-- contact -->
<div class="abs field" style="left:70px;top:3316px;width:302px;height:61px">Name</div>
<div class="abs field" style="left:386px;top:3316px;width:302px;height:61px">Email</div>
<div class="abs field" style="left:70px;top:3394px;width:618px;height:171px">Message</div>
<div class="abs btn btn-fill" style="left:296px;top:3583px;width:154px;height:50px;font-size:16px">Contact US</div>
<div class="abs contact-art" role="img" aria-label="Illustration of people beside large location, mail and phone bubbles among trees"></div>
<h2 class="abs display" style="left:790px;top:3312px;width:314px;text-align:center;font-size:30px;color:var(--blue-sky)">Contact US</h2>

<!-- footer -->
<footer class="abs footer"></footer>
<div class="abs brand footer-brand"><span class="brand-dot"></span>BRIGHT LANTERN</div>
<div class="abs col" style="left:43px"><h4>More links</h4>Home<br>Career<br>Contact<br>Imprint<br>Data protection</div>
<div class="abs col" style="left:253px"><h4>Case study</h4>Pawcrest<br>Ilse Moran<br>Stride Gym Hagen<br>Medpost</div>
<div class="abs col" style="left:460px"><h4>Contact</h4>+49 211 555 0142<br>hello@brightlantern.de</div>
<div class="abs footer-art" role="img" aria-label="Illustration of two people beside a large board with message icons"></div>
<div class="abs footer-rule"></div>
<div class="abs copyright">Bright Lantern 2020. All Rights Reserved.</div>

</body>
</html>
```